qrm Process Solutions
we're in control
Professional
gerald p whitcomb
584 ravenmoor lane bakersfield, ca 93308
gerry@qrmprocessworks.example
qrmprocessworks.example
purpose: we create success by achieving what others cannot. vision: creating value that is unsurpassed with best in class process performance. inspired and respected community member values: accountability, honesty, integrity, respect, passion, improvement

```html
<!DOCTYPE html>
<html lang="en">
<head>
<meta charset="utf-8">
<title>qrm Process Solutions – Business Card</title>
<link href="https://fonts.googleapis.com/css2?family=Arimo:wght@400;700&display=swap" rel="stylesheet">
<style>
  :root {
    --navy: #16286b;
    --red: #e0262b;
    --border: #c9c9c9;
    --page: #ffffff;
  }
  * { box-sizing: border-box; margin: 0; padding: 0; }
  html, body {
    width: 1200px; height: 334px; overflow: hidden;
    background: var(--page);
    font-family: "Arimo", Arial, sans-serif;
    color: var(--navy);
  }
  .sheet { position: relative; width: 1200px; height: 334px; }
  .card {
    position: absolute; top: 2px;
    width: 583px; height: 330px;
    border: 1px solid var(--border);
    background: #fff; overflow: hidden;
  }
  .card--front { left: 0; }
  .card--back { left: 617px; }
  .swoosh { position: absolute; inset: 0; width: 100%; height: 100%; }
  .company {
    position: absolute; left: 60px; top: 40px;
    width: 150px;
    font-size: 22px; line-height: 26px; font-weight: 400;
    color: var(--navy);
  }
  .holder {
    position: absolute; left: 346px; top: 22px;
    font-size: 17px; font-weight: 700; color: var(--navy);
  }
  .contact {
    position: absolute; left: 200px; top: 222px;
    display: grid; grid-template-columns: 90px auto;
    column-gap: 4px;
    font-size: 15px; line-height: 20px;
  }
  .contact__label { color: var(--red); text-align: right; }
  .contact__value { color: var(--navy); white-space: nowrap; }
  .statement {
    position: absolute; left: 175px; top: 194px; width: 360px;
    font-size: 11.5px; line-height: 14px;
  }
  .statement__head { color: var(--red); font-size: 13px; }
  .statement__body { color: var(--navy); }
</style>
</head>
<body>
<div class="sheet">
  <section class="card card--front">
    <svg class="swoosh" viewBox="0 0 583 330" preserveAspectRatio="none" aria-hidden="true">
      <defs>
        <linearGradient id="navyFront" x1="0" y1="0" x2="1" y2="1">
          <stop offset="0" stop-color="#2a4aa0"/>
          <stop offset="1" stop-color="#0b1a52"/>
        </linearGradient>
      </defs>
      <path d="M0,0 L34,0 C8,120 40,250 240,330 L0,330 Z" fill="url(#navyFront)"/>
      <path d="M34,0 C14,120 50,240 260,330" fill="none" stroke="#5b7fcf" stroke-width="3"/>
    </svg>
    <div class="company">qrm Process Solutions</div>
    <h1 class="holder">Gerald P Whitcomb</h1>
    <div class="contact">
      <span class="contact__label">Add :</span><span class="contact__value">584 ravenmoor lane bakersfield,</span>
      <span></span><span class="contact__value">ca 93308</span>
      <span class="contact__label">Ph :</span><span class="contact__value">6615550172</span>
      <span class="contact__label">Email :</span><span class="contact__value">gerry@qrmprocessworks.example</span>
      <span class="contact__label">Web :</span><span class="contact__value">qrmprocessworks.example</span>
    </div>
  </section>

  <section class="card card--back">
    <svg class="swoosh" viewBox="0 0 583 330" preserveAspectRatio="none" aria-hidden="true">
      <defs>
        <linearGradient id="navyBack" x1="0" y1="0" x2="1" y2="1">
          <stop offset="0" stop-color="#2a4aa0"/>
          <stop offset="1" stop-color="#0b1a52"/>
        </linearGradient>
      </defs>
      <path d="M0,0 L34,0 C8,120 40,250 240,330 L0,330 Z" fill="url(#navyBack)"/>
      <path d="M34,0 C14,120 50,240 260,330" fill="none" stroke="#5b7fcf" stroke-width="3"/>
    </svg>
    <div class="company">qrm Process Solutions</div>
    <div class="statement">
      <div class="statement__head">Purpose</div>
      <div class="statement__body">we create success by achieving what others cannot.</div>
      <div class="statement__head">Vision</div>
      <div class="statement__body">creating value that is unsurpassed with best in class process performance. inspired and respected community member</div>
      <div class="statement__head">Values</div>
      <div class="statement__body">accountability, honesty, integrity, respect, passion, improvement</div>
    </div>
  </section>
</div>
</body>
</html>
```